ODE Sapphire Harbor Sell Sheet

We need a two-sided portrait-style sell sheet for a new insurance product called the ODE Sapphire Harbor. The ODE Sapphire Harbor is a custom Executive Risk commercial insurance policy that provides the broadest level of protection available in the marketplace. The sell sheet would primarily use the colors blue, gray and white, have clean lines, minimal graphics (perhaps a picture of an executive boardroom at the top), three boxes (or text areas) to provide a brief description of the specific insurance products provided by the Sapphire (Directors & Officers Liability, Employment Practices Liability, and Fiduciary Liability), be easy to read and really pique the reader's interest to learn more about the product. The title (ODE Sapphire Harbor) would overlay the graphic at the top, and just below the title would be the phrase "Coverage Beyond the Standard", which is our tagline for the product. There would be a two-sentence lead-in phrase just below the graphic ("Sapphire Harbor is an exclusive, custom-designed insurance policy tailored to a company’s specific risk profile. The policy was created to provide clients with a premium, industry-leading level of protection not found in the standard insurance marketplace". There needs to be another text section entitled "Return on Investment" and capable of containing three medium length sentences. There needs to be an "About Us" section (three to four medium-length sentences) and a "Contact Us" section (contact name, phone (x2), e-mail, address). On the back we want to discuss the specific features of the product by section of the policy (General Terms and Conditions, Directors & Officers Liability Insurance, Employment Practices Liability Insurance, Fiduciary Liability Insurance. This would likely be set out in bullet format.

I have attached a few examples found on the web that are similar to my vision for this sell sheet, but none that exactly fit our needs (whether graphically or due to specific layout).

Industry/Entity Type

Insurance

Font styles to use
Serif

Requirements
Must have
• I have uploaded a sample done in powerpoint. Please disregard the coloring as I did not have time to choose colors. I did not add the "About Us" and "Contact Us" sections on the front page and would like creative ideas on structuring that. On the back page, I think a nice looking table broken down by section of the policy would look nice, and allow us to enter bulleted coverage features for each section. Both graphics in the sample were found on google without watermarks by searching "board room" and "business agreement", respectively.

```html
<!DOCTYPE html>
<html lang="en">
<head>
<meta charset="utf-8">
<title>ODE Sapphire Harbor Sell Sheet</title>
<link rel="stylesheet" href="https://fonts.googleapis.com/css2?family=Montserrat:wght@500;600;700&family=Lato:wght@400;700&display=swap">
<style>
  :root {
    --blue: #17a6e6;
    --blue-deep: #0a7fc4;
    --ink: #1f1f1f;
    --gray: #6b6b6b;
    --gray-dark: #555;
    --paper: #ffffff;
    --stage: #d2d2d2;
  }
  * { box-sizing: border-box; margin: 0; padding: 0; }
  html, body { width: 1200px; height: 1200px; overflow: hidden; }
  body {
    background: radial-gradient(circle at 50% 45%, #e6e6e6, var(--stage));
    font-family: "Lato", sans-serif;
    color: var(--ink);
    position: relative;
  }
  .page {
    position: absolute;
    top: 175px;
    width: 545px;
    height: 764px;
    background: var(--paper);
    box-shadow: 0 3px 10px rgba(0,0,0,.28);
    overflow: hidden;
  }
  .page--front { left: 36px; }
  .page--back { left: 614px; background: #f1f1f1; }

  /* front header */
  .hero { position: absolute; left: 0; top: 0; width: 545px; height: 230px; }
  .hero__title {
    position: absolute; top: 78px; left: 0; width: 545px; text-align: center;
    font-family: "Montserrat", sans-serif; font-weight: 700; font-size: 29px;
    color: #fff; letter-spacing: .3px;
  }
  .hero__tagline {
    position: absolute; top: 120px; left: 0; width: 545px; text-align: center;
    font-family: "Lato", sans-serif; font-weight: 400; font-size: 14px;
    letter-spacing: 2px; color: #e6f4fb;
  }
  .intro {
    position: absolute; top: 265px; left: 10px; width: 525px;
    font-size: 12.2px; line-height: 15.5px; text-align: justify;
  }

  .sidebar {
    position: absolute; left: 10px; top: 339px; width: 203px; height: 318px;
    background: var(--blue); color: #fff; padding: 16px 9px 0 9px;
  }
  .sidebar h2 {
    font-family: "Montserrat", sans-serif; font-size: 16px; font-weight: 600; margin: 0 0 5px 0;
  }
  .sidebar p { font-size: 9.4px; line-height: 12px; text-align: justify; color: #e9f6fd; }
  .sidebar hr { border: 0; border-top: 1.5px solid #fff; margin: 12px 0 6px; }

  .products { position: absolute; left: 224px; top: 346px; width: 306px; }
  .product { border-top: 2px solid var(--blue); padding-top: 5px; margin-bottom: 11px; }
  .product__label {
    display: inline-block; background: var(--blue); color: #fff;
    font-family: "Montserrat", sans-serif; font-weight: 600; font-size: 10.4px;
    padding: 3px 4px; position: relative; margin-right: 14px;
  }
  .product__label::after {
    content: ""; position: absolute; right: -11px; top: 0; width: 6px; height: 100%;
    background: var(--gray-dark); transform: skewX(-20deg);
  }
  .product p { font-size: 8.6px; line-height: 11px; text-align: justify; margin-top: 10px; }

  /* footer */
  .footer { position: absolute; left: 0; bottom: 0; width: 545px; height: 80px; }
  .footer__info { position: absolute; left: 0; bottom: 0; width: 545px; height: 58px; color: #fff; }
  .footer__name {
    position: absolute; top: 2px; width: 100%; text-align: center;
    font-family: "Montserrat", sans-serif; font-weight: 600; font-size: 16px;
  }
  .footer__item { position: absolute; font-family: "Montserrat", sans-serif; font-weight: 600; font-size: 7.6px; line-height: 10px; display: flex; gap: 5px; }
  .footer__item svg { flex: none; margin-top: 1px; }
  .footer__addr { left: 16px; top: 29px; }
  .footer__phone { left: 222px; top: 28px; letter-spacing: 2px; }
  .footer__mail { left: 382px; top: 29px; }

  /* back */
  .back__bar { position: absolute; left: 0; top: 0; width: 545px; height: 28px; background: #6b6b6b; }
  .features {
    position: absolute; left: 20px; top: 49px; width: 510px; height: 610px;
    display: grid; grid-template-columns: 119px 133px 142px 116px;
    border: 1px solid #777; background: rgba(255,255,255,.55);
  }
  .features__col { border-right: 1.5px solid #777; }
  .features__col:last-child { border-right: 0; }
  .features__head {
    height: 32px; background: var(--blue); color: #fff; text-align: center;
    font-family: "Montserrat", sans-serif; font-weight: 600; font-size: 8.4px; line-height: 10px;
    display: flex; align-items: center; justify-content: center; padding: 0 4px;
  }
  .features ul { list-style: none; padding: 28px 9px 0 8px; }
  .features li {
    font-size: 6.5px; line-height: 9.2px; text-transform: uppercase; text-align: justify;
    margin-bottom: 9.5px;
  }
  .features li::before { content: "➤ "; color: var(--blue); font-size: 5px; }
</style>
</head>
<body>

<!-- FRONT -->
<section class="page page--front">
  <div class="hero">
    <svg width="545" height="230" viewBox="0 0 545 230" role="img" aria-label="Photo of an executive boardroom with a long table and leather chairs">
      <defs>
        <linearGradient id="room" x1="0" y1="0" x2="1" y2="1">
          <stop offset="0" stop-color="#4a4f56"/>
          <stop offset=".5" stop-color="#2e3238"/>
          <stop offset="1" stop-color="#6a625a"/>
        </linearGradient>
      </defs>
      <path d="M0 0H545V176C420 200 300 228 160 224C90 222 40 214 0 208Z" fill="url(#room)"/>
      <path d="M0 208C40 214 90 222 160 224C300 228 420 200 545 176" fill="none" stroke="var(--blue)" stroke-width="5"/>
    </svg>
    <h1 class="hero__title">ODE SAPPHIRE HARBOR</h1>
    <div class="hero__tagline">COVERAGE BEYOND THE STANDARD</div>
  </div>

  <p class="intro">Sapphire Harbor is an exclusive, custom-designed insurance policy tailored to a company’s specific risk profile. The policy was created to provide clients with a premium, industry-leading level of protection not found in the standard insurance marketplace</p>

  <aside class="sidebar">
    <h2>About us</h2>
    <p>Lorem ipsum dolor sit amet, consectetuer adipiscing elit. Aenean commodo ligula eget dolor. Aenean massa. Cum sociis natoque penatibus et magnis dis parturient montes, nascetur ridiculus mus.Lorem ipsum dolor sit amet, consectetuer adipiscing elit. Aenean commodo ligula eget dolor. Aenean massa. Cum sociis natoque penatibus et magnis dis parturient montes, nascetur ridiculus mus.</p>
    <hr>
    <h2>Return on Investment</h2>
    <p>Lorem ipsum dolor sit amet, consectetuer adipiscing elit. Aenean commodo ligula eget dolor. Aenean massa. Cum sociis natoque penatibus et magnis dis parturient montes, nascetur ridiculus mus.Lorem ipsum dolor sit amet, consectetuer adipiscing elit. Aenean commodo ligula eget dolor. Aenean massa. Cum sociis natoque penatibus et magnis dis parturient montes, nascetur ridiculus mus.</p>
  </aside>

  <div class="products">
    <article class="product">
      <span class="product__label">Directors &amp; Officers Liability</span>
      <p>Lorem ipsum dolor sit amet, consectetuer adipiscing elit. Aenean commodo ligula eget dolor. Aenean massa. Cum sociis natoque penatibus et magnis dis parturient montes, nascetur ridiculus mus.Lorem ipsum dolor sit amet, consectetuer adipiscing elit. Aenean commodo ligula eget dolor. Aenean massa. Cum sociis natoque penatibus et magnis dis parturient montes, nascetur ridiculus mus.</p>
    </article>
    <article class="product">
      <span class="product__label">Employment Practices Liability</span>
      <p>Lorem ipsum dolor sit amet, consectetuer adipiscing elit. Aenean commodo ligula eget dolor. Aenean massa. Cum sociis natoque penatibus et magnis dis parturient montes, nascetur ridiculus mus.Lorem ipsum dolor sit amet, consectetuer adipiscing elit. Aenean commodo ligula eget dolor. Aenean massa. Cum sociis natoque penatibus et magnis dis parturient montes, nascetur ridiculus mus.</p>
    </article>
    <article class="product">
      <span class="product__label">Fiduciary Liability</span>
      <p>Lorem ipsum dolor sit amet, consectetuer adipiscing elit. Aenean commodo ligula eget dolor. Aenean massa. Cum sociis natoque penatibus et magnis dis parturient montes, nascetur ridiculus mus.Lorem ipsum dolor sit amet, consectetuer adipiscing elit. Aenean commodo ligula eget dolor. Aenean massa. Cum sociis natoque penatibus et magnis dis parturient montes, nascetur ridiculus mus.</p>
    </article>
  </div>

  <footer class="footer">
    <svg width="545" height="80" viewBox="0 0 545 80" role="img" aria-label="Contact band with a faint photo of business people in blue tones">
      <path d="M0 16C180 -4 360 -4 545 16V80H0Z" fill="#6e6e6e"/>
      <path d="M0 22C180 4 360 4 545 22V80H0Z" fill="var(--blue)"/>
    </svg>
    <div class="footer__info">
      <div class="footer__name">CONTACT NAME</div>
      <div class="footer__item footer__addr">
        <svg width="7" height="9" viewBox="0 0 7 9"><path d="M3.5 0A3.2 3.2 0 0 0 .3 3.2C.3 5.6 3.5 9 3.5 9S6.7 5.6 6.7 3.2A3.2 3.2 0 0 0 3.5 0Zm0 4.5a1.3 1.3 0 1 1 0-2.6 1.3 1.3 0 0 1 0 2.6Z" fill="#fff"/></svg>
        <span>Lorem ipsum dolor sit amet,<br>Lorem ipsum, 12345</span>
      </div>
      <div class="footer__item footer__phone">
        <svg width="7" height="7" viewBox="0 0 7 7"><path d="M1.4 0 2.6 1.6 1.9 2.4C2.4 3.5 3.3 4.4 4.5 5L5.3 4.3 7 5.5 6.2 7C2.6 6.7.2 4.2 0 .8Z" fill="#fff"/></svg>
        <span>555-014-2236<br>555-017-8840</span>
      </div>
      <div class="footer__item footer__mail">
        <svg width="8" height="6" viewBox="0 0 8 6"><rect width="8" height="6" fill="#fff"/><path d="M0 0 4 3.2 8 0" fill="none" stroke="var(--blue)" stroke-width=".8"/></svg>
        <span>info@odesapphireharbor.com</span>
      </div>
    </div>
  </footer>
</section>

<!-- BACK -->
<section class="page page--back">
  <div class="back__bar"></div>
  <div class="features">
    <div class="features__col">
      <div class="features__head">GENERAL TERMS AND CONDITIONS</div>
      <ul>
        <li>Lorem ipsum dolor sit amet, consectetuer adipiscing elit. Aenean commodo ligula eget dolor. Aenean massa.</li>
        <li>Cum sociis natoque penatibus et magnis dis parturient montes, nascetur ridiculus mus. Donec quam felis, ultricies nec, pellentesque eu, pretium quis, sem.</li>
        <li>Nulla consequat massa quis enim. Donec pede justo, fringilla vel, aliquet nec, vulputate eget, arcu.</li>
        <li>In enim justo, rhoncus ut, imperdiet a, venenatis vitae, justo. Nullam dictum felis eu pede mollis pretium. Integer tincidunt. Cras dapibus.</li>
        <li>Vivamus elementum semper nisi. Aenean vulputate eleifend tellus. Aenean leo ligula, porttitor eu, consequat vitae, eleifend ac, enim.</li>
        <li>Aliquam lorem ante, dapibus in, viverra quis, feugiat a, tellus. Phasellus viverra nulla ut metus varius laoreet. Quisque rutrum. Aenean imperdiet.</li>
        <li>Etiam ultricies nisi vel augue. Curabitur ullamcorper ultricies nisi. Nam eget dui. Etiam rhoncus.</li>
        <li>Maecenas tempus, tellus eget condimentum rhoncus, sem quam semper libero, sit amet adipiscing sem neque sed ipsum. Nam quam nunc, blandit vel, luctus pulvinar, hendrerit id, lorem.</li>
      </ul>
    </div>
    <div class="features__col">
      <div class="features__head">DIRECTORS &amp; OFFICERS LIABILITY INSURANCE</div>
      <ul>
        <li>Lorem ipsum dolor sit amet, consectetuer adipiscing elit. Aenean commodo ligula eget dolor. Aenean massa.</li>
        <li>Cum sociis natoque penatibus et magnis dis parturient montes, nascetur ridiculus mus. Donec quam felis, ultricies nec, pellentesque eu, pretium quis, sem.</li>
        <li>Nulla consequat massa quis enim. Donec pede justo, fringilla vel, aliquet nec, vulputate eget, arcu.</li>
        <li>In enim justo, rhoncus ut, imperdiet a, venenatis vitae, justo. Nullam dictum felis eu pede mollis pretium. Integer tincidunt. Cras dapibus.</li>
        <li>Vivamus elementum semper nisi. Aenean vulputate eleifend tellus. Aenean leo ligula, porttitor eu, consequat vitae, eleifend ac, enim.</li>
        <li>Aliquam lorem ante, dapibus in, viverra quis, feugiat a, tellus. Phasellus viverra nulla ut metus varius laoreet. Quisque rutrum. Aenean imperdiet.</li>
        <li>Etiam ultricies nisi vel augue. Curabitur ullamcorper ultricies nisi. Nam eget dui. Etiam rhoncus.</li>
        <li>Maecenas tempus, tellus eget condimentum rhoncus, sem quam semper libero, sit amet adipiscing sem neque sed ipsum. Nam quam nunc, blandit vel, luctus pulvinar, hendrerit id, lorem.</li>
      </ul>
    </div>
    <div class="features__col">
      <div class="features__head">EMPLOYMENT PRACTICES LIABILITY INSURANCE</div>
      <ul>
        <li>Lorem ipsum dolor sit amet, consectetuer adipiscing elit. Aenean commodo ligula eget dolor. Aenean massa.</li>
        <li>Cum sociis natoque penatibus et magnis dis parturient montes, nascetur ridiculus mus. Donec quam felis, ultricies nec, pellentesque eu, pretium quis, sem.</li>
        <li>Nulla consequat massa quis enim. Donec pede justo, fringilla vel, aliquet nec, vulputate eget, arcu.</li>
        <li>In enim justo, rhoncus ut, imperdiet a, venenatis vitae, justo. Nullam dictum felis eu pede mollis pretium. Integer tincidunt. Cras dapibus.</li>
        <li>Vivamus elementum semper nisi. Aenean vulputate eleifend tellus. Aenean leo ligula, porttitor eu, consequat vitae, eleifend ac, enim.</li>
        <li>Aliquam lorem ante, dapibus in, viverra quis, feugiat a, tellus. Phasellus viverra nulla ut metus varius laoreet. Quisque rutrum. Aenean imperdiet.</li>
        <li>Etiam ultricies nisi vel augue. Curabitur ullamcorper ultricies nisi. Nam eget dui. Etiam rhoncus.</li>
        <li>Maecenas tempus, tellus eget condimentum rhoncus, sem quam semper libero, sit amet adipiscing sem neque sed ipsum. Nam quam nunc, blandit vel, luctus pulvinar, hendrerit id, lorem.</li>
      </ul>
    </div>
    <div class="features__col">
      <div class="features__head">FIDUCIARY LIABILITY INSURANCE</div>
      <ul>
        <li>Lorem ipsum dolor sit amet, consectetuer adipiscing elit. Aenean commodo ligula eget dolor. Aenean massa.</li>
        <li>Cum sociis natoque penatibus et magnis dis parturient montes, nascetur ridiculus mus. Donec quam felis, ultricies nec, pellentesque eu, pretium quis, sem.</li>
        <li>Nulla consequat massa quis enim. Donec pede justo, fringilla vel, aliquet nec, vulputate eget, arcu.</li>
        <li>In enim justo, rhoncus ut, imperdiet a, venenatis vitae, justo. Nullam dictum felis eu pede mollis pretium. Integer tincidunt. Cras dapibus.</li>
        <li>Vivamus elementum semper nisi. Aenean vulputate eleifend tellus. Aenean leo ligula, porttitor eu, consequat vitae, eleifend ac, enim.</li>
        <li>Aliquam lorem ante, dapibus in, viverra quis, feugiat a, tellus. Phasellus viverra nulla ut metus varius laoreet. Quisque rutrum. Aenean imperdiet.</li>
        <li>Etiam ultricies nisi vel augue. Curabitur ullamcorper ultricies nisi. Nam eget dui. Etiam rhoncus.</li>
        <li>Maecenas tempus, tellus eget condimentum rhoncus, sem quam semper libero, sit amet adipiscing sem neque sed ipsum. Nam quam nunc, blandit vel, luctus pulvinar, hendrerit id, lorem.</li>
      </ul>
    </div>
  </div>

  <footer class="footer">
    <svg width="545" height="80" viewBox="0 0 545 80" role="img" aria-label="Contact band with a faint photo of business people in blue tones">
      <path d="M0 16C180 -4 360 -4 545 16V80H0Z" fill="#6e6e6e"/>
      <path d="M0 22C180 4 360 4 545 22V80H0Z" fill="var(--blue)"/>
    </svg>
    <div class="footer__info">
      <div class="footer__name">CONTACT NAME</div>
      <div class="footer__item footer__addr">
        <svg width="7" height="9" viewBox="0 0 7 9"><path d="M3.5 0A3.2 3.2 0 0 0 .3 3.2C.3 5.6 3.5 9 3.5 9S6.7 5.6 6.7 3.2A3.2 3.2 0 0 0 3.5 0Zm0 4.5a1.3 1.3 0 1 1 0-2.6 1.3 1.3 0 0 1 0 2.6Z" fill="#fff"/></svg>
        <span>Lorem ipsum dolor sit amet,<br>Lorem ipsum, 12345</span>
      </div>
      <div class="footer__item footer__phone">
        <svg width="7" height="7" viewBox="0 0 7 7"><path d="M1.4 0 2.6 1.6 1.9 2.4C2.4 3.5 3.3 4.4 4.5 5L5.3 4.3 7 5.5 6.2 7C2.6 6.7.2 4.2 0 .8Z" fill="#fff"/></svg>
        <span>555-014-2236<br>555-017-8840</span>
      </div>
      <div class="footer__item footer__mail">
        <svg width="8" height="6" viewBox="0 0 8 6"><rect width="8" height="6" fill="#fff"/><path d="M0 0 4 3.2 8 0" fill="none" stroke="var(--blue)" stroke-width=".8"/></svg>
        <span>info@odesapphireharbor.com</span>
      </div>
    </div>
  </footer>
</section>

</body>
</html>
```